Harborline Toma's Chinese/Dim Sum Restaurant Menu

Harborline Toma's is a seafood-asian fusion restaurant featuring dim sum and other classical asian fusion items.

We need a menu design that includes both our food menu and our drink menu.

Food menu: Needs to have space for descriptions of food (please just include a place holder and we will input them later). See attached for food menu items.

Drink menu: Just lists of items with prices. See attached Jade Lantern Menu- please include the same items, but rebrand for Harborline Toma's.

The menus must be able to be printed in a 4.25x11in paper.

We want something modern and contemporary. My boss likes geometrical design aspects and minimalism. So, nothing too ornate. But, it has to be different from the Jade Lantern menus. Colors can be black, red, gold or blue- but it must be able to be tied into our black and red Harborline Toma's logo. Including elements of Chinese culture, especially fishing, is a plus, but not necessary.

We also need this in ai format when we download final copy so we can edit in the future.

UPDATE: Please note, we already have a logo.

Target Market(s)

Upscale family diners

Industry/Entity Type

Chinese Food

Font styles to use
Serif
Sans Serif

Colors
0054AA
0677BA
7BADD7
CADEEF
E8F1F8
0094D4
00A9DD
6FCCEA
C7EBF8
E9F6FB
FFC000
F8CF3A
FAE287
FDF2CF
FEFAEE
EB3D1F
EC4F4E
F09395
F8D3D4
FCEDEE

Requirements
Must have
• Classic, minimalist, elegant

```html
<!DOCTYPE html>
<html lang="en">
<head>
<meta charset="utf-8">
<title>Harborline Toma's — Food &amp; Drink Menus</title>
<link rel="stylesheet" href="https://fonts.googleapis.com/css2?family=Oswald:wght@600&family=Playfair+Display:ital,wght@0,700;1,600&family=Montserrat:wght@500;700&display=swap">
<style>
:root{
  --red:#e23a22;
  --red-deep:#c62f1a;
  --gold:#f8c33a;
  --gold-deep:#e9a92a;
  --gold-soft:#fae287;
  --cream:#fdf2cf;
  --ivory:#fefaee;
  --ink:#3b2a18;
  --page:#efefef;
  --white:#ffffff;
}
*{box-sizing:border-box;margin:0;padding:0}
html,body{width:814px;height:1200px;overflow:hidden;background:var(--page)}
.canvas{position:relative;width:814px;height:1200px;overflow:hidden;
  background:linear-gradient(180deg,#f3f3f3,#ebebeb);font-family:"Montserrat",sans-serif;color:var(--ink)}
.panel{position:absolute;width:103px;overflow:hidden;display:flex;flex-direction:column;gap:5px;padding:10px 8px}
.row-food .panel{top:14px;height:340px}
.row-drink .panel{top:380px;height:440px}
.row-liquor .panel{top:832px;height:360px}

.panel.food{background:var(--red);box-shadow:inset 0 0 0 3px var(--red),inset 0 0 0 4px var(--gold)}
.panel.drink{background:var(--white);box-shadow:0 0 0 1px #e2e2e2,inset 0 0 0 4px var(--white),inset 0 0 0 5px var(--gold)}

/* brand */
.brand{display:flex;flex-direction:column;align-items:center;font-family:"Oswald",sans-serif;font-weight:600;line-height:1;text-align:center}
.brand .mark{width:9px;height:9px;border-radius:50%;margin-bottom:3px}
.brand .name{font-size:10px;letter-spacing:.5px}
.brand .sub{font-size:6px;letter-spacing:2px}
.food .brand{color:var(--white)}
.food .brand .mark{background:var(--white)}
.drink .brand{color:var(--red)}
.drink .brand .mark{background:var(--red)}
.brand.mini .name{font-size:8px}
.brand.mini .sub{font-size:5px}
.brand.mini .mark{width:6px;height:6px;margin-bottom:2px}

/* covers */
.cover{justify-content:flex-start;align-items:center}
.lantern{width:22px;height:30px;border-radius:45% 45% 40% 40%;background:linear-gradient(180deg,var(--gold),var(--gold-deep));align-self:flex-start;margin-top:4px}
.cover .brand{margin-top:62px}
.cover .brand .name{font-size:13px}
.cover .brand .sub{font-size:7px}
.dots{display:flex;gap:4px;margin-top:6px}
.dots i{width:6px;height:6px;border-radius:50%;background:var(--ink)}
.food .dots i{background:#7a1a0c}
.cover .label{font-family:"Playfair Display",serif;font-style:italic;font-weight:600;font-size:16px;color:var(--gold);margin-top:6px;letter-spacing:1px}
.info-card{margin-top:auto;width:72px;background:var(--white);padding:4px;font-size:3.6px;line-height:1.6;color:var(--ink)}
.info-card p{border-bottom:.5px solid #d9d9d9}

/* sections */
.section-title{font-family:"Playfair Display",serif;font-weight:700;font-size:7.5px;letter-spacing:.4px;line-height:1}
.food .section-title{color:var(--gold)}
.drink .section-title{color:var(--red);font-size:8px}
.section-title small{font-family:"Montserrat",sans-serif;font-weight:500;font-size:3.6px;color:var(--gold-deep);letter-spacing:.3px;margin-left:3px}

.menu-table{list-style:none;background:var(--ivory);font-size:4px;line-height:1}
.menu-table li{display:flex;justify-content:space-between;padding:1.4px 3px;border-bottom:.5px solid var(--gold-soft)}
.menu-table li.head{background:var(--gold);font-weight:700;font-size:3.6px;letter-spacing:.3px;border:none}
.menu-table li b{font-weight:700}
.drink .menu-table{background:var(--gold-soft)}
.drink .menu-table li{padding:1.8px 3px;border-bottom:.5px solid var(--gold)}
.drink .menu-table li:nth-child(even){background:var(--cream)}
.drink .menu-table li.head{background:var(--gold-deep);color:var(--white)}

.photo{height:40px;border:1px solid var(--gold);background:linear-gradient(135deg,#4a2c18,#9c5d26 55%,#d99a3c)}
.photo.tall{height:52px}
</style>
</head>
<body>
<main class="canvas">

  <!-- FOOD MENU -->
  <section class="row-food">
    <article class="panel food cover" style="left:95px">
      <div class="lantern" role="img" aria-label="Hanging gold lantern ornament"></div>
      <div class="brand"><span class="mark"></span><span class="name">HARBORLINE</span><span class="sub">TOMA'S</span></div>
      <div class="dots"><i></i><i></i><i></i></div>
      <p class="label">FOOD</p>
      <div class="info-card"><p>12 Pier Lane, Bay City</p><p>Tel 555-0142</p><p>Open daily 11am–10pm</p></div>
    </article>

    <article class="panel food" style="left:220px">
      <h2 class="section-title">DIM SUM</h2>
      <ul class="menu-table">
        <li class="head"><span>ITEMS</span><span>PRICE</span></li>
        <li><span>Shrimp Har Gow</span><b>$7</b></li>
        <li><span>Pork Siu Mai</span><b>$6</b></li>
        <li><span>Char Siu Bao</span><b>$6</b></li>
        <li><span>Crystal Dumplings</span><b>$7</b></li>
        <li><span>Rice Noodle Roll</span><b>$6</b></li>
        <li><span>Turnip Cake</span><b>$5</b></li>
        <li><span>Chicken Feet</span><b>$5</b></li>
        <li><span>Custard Tart</span><b>$5</b></li>
      </ul>
      <div class="photo" role="img" aria-label="Photo of steamed dim sum in a bamboo basket"></div>
      <h2 class="section-title">SOUP</h2>
      <ul class="menu-table">
        <li class="head"><span>ITEMS</span><span>PRICE</span></li>
        <li><span>Hot and Sour</span><b>$6</b></li>
        <li><span>Wonton Soup</span><b>$6</b></li>
        <li><span>Seafood Tofu</span><b>$8</b></li>
        <li><span>Egg Drop</span><b>$5</b></li>
      </ul>
      <div class="photo tall" role="img" aria-label="Photo of a bowl of seafood soup"></div>
    </article>

    <article class="panel food" style="left:345px">
      <h2 class="section-title">APPETIZERS</h2>
      <ul class="menu-table">
        <li class="head"><span>ITEMS</span><span>PRICE</span></li>
        <li><span>Spring Rolls</span><b>$6</b></li>
        <li><span>Crab Rangoon</span><b>$7</b></li>
        <li><span>Salt Pepper Squid</span><b>$9</b></li>
        <li><span>Scallion Pancake</span><b>$6</b></li>
        <li><span>Potstickers</span><b>$7</b></li>
        <li><span>Edamame</span><b>$5</b></li>
        <li><span>Pork Ribs</span><b>$9</b></li>
        <li><span>Fried Calamari</span><b>$9</b></li>
        <li><span>Lettuce Wraps</span><b>$8</b></li>
      </ul>
      <div class="photo" role="img" aria-label="Photo of fried appetizers on a plate"></div>
      <h2 class="section-title">RICE AND NOODLES</h2>
      <ul class="menu-table">
        <li class="head"><span>ITEMS</span><span>PRICE</span></li>
        <li><span>Yang Chow Rice</span><b>$11</b></li>
        <li><span>Seafood Lo Mein</span><b>$13</b></li>
        <li><span>Beef Chow Fun</span><b>$12</b></li>
        <li><span>Singapore Noodles</span><b>$12</b></li>
        <li><span>Crab Fried Rice</span><b>$14</b></li>
        <li><span>Pan Fried Noodles</span><b>$12</b></li>
      </ul>
      <div class="photo" role="img" aria-label="Photo of fried noodles and rice dishes"></div>
    </article>

    <article class="panel food" style="left:470px">
      <h2 class="section-title">SEAFOOD</h2>
      <ul class="menu-table">
        <li class="head"><span>ITEMS</span><span>PRICE</span></li>
        <li><span>Lobster Ginger</span><b>$32</b></li>
        <li><span>Steamed Sea Bass</span><b>$26</b></li>
        <li><span>Honey Walnut Prawns</span><b>$19</b></li>
        <li><span>Black Bean Clams</span><b>$17</b></li>
        <li><span>Salt Pepper Shrimp</span><b>$18</b></li>
        <li><span>Kung Pao Scallops</span><b>$21</b></li>
        <li><span>Crab Curry</span><b>$28</b></li>
        <li><span>Mussels XO</span><b>$17</b></li>
      </ul>
      <h2 class="section-title">VEGGIE</h2>
      <ul class="menu-table">
        <li class="head"><span>ITEMS</span><span>PRICE</span></li>
        <li><span>Garlic Bok Choy</span><b>$9</b></li>
        <li><span>Mapo Tofu</span><b>$10</b></li>
        <li><span>Dry Green Beans</span><b>$9</b></li>
        <li><span>Buddha Delight</span><b>$11</b></li>
      </ul>
      <h2 class="section-title">SWEET &amp; DESSERT</h2>
      <ul class="menu-table">
        <li class="head"><span>ITEMS</span><span>PRICE</span></li>
        <li><span>Mango Pudding</span><b>$6</b></li>
        <li><span>Sesame Balls</span><b>$6</b></li>
        <li><span>Red Bean Soup</span><b>$5</b></li>
        <li><span>Fried Banana</span><b>$6</b></li>
      </ul>
      <div class="photo tall" role="img" aria-label="Photo of seafood and vegetable dishes"></div>
    </article>
  </section>

  <!-- DRINK MENU -->
  <section class="row-drink">
    <article class="panel drink cover" style="left:54px">
      <div class="lantern" role="img" aria-label="Hanging gold lantern ornament"></div>
      <div class="brand"><span class="mark"></span><span class="name">HARBORLINE</span><span class="sub">TOMA'S</span></div>
      <div class="dots"><i></i><i></i><i></i></div>
      <p class="label">DRINK</p>
    </article>

    <article class="panel drink" style="left:190px">
      <div class="brand mini"><span class="mark"></span><span class="name">HARBORLINE</span><span class="sub">TOMA'S</span></div>
      <h2 class="section-title">DESSERTS</h2>
      <ul class="menu-table">
        <li class="head"><span>ITEMS</span><span>PRICE</span></li>
        <li><span>Egg Tart</span><b>$5</b></li>
        <li><span>Mango Pudding</span><b>$6</b></li>
        <li><span>Sesame Balls</span><b>$6</b></li>
        <li><span>Lychee Sorbet</span><b>$6</b></li>
        <li><span>Almond Jelly</span><b>$5</b></li>
      </ul>
      <h2 class="section-title">HOT BEVERAGES</h2>
      <ul class="menu-table">
        <li class="head"><span>ITEMS</span><span>PRICE</span></li>
        <li><span>Jasmine Tea</span><b>$3</b></li>
        <li><span>Oolong Tea</span><b>$3</b></li>
        <li><span>Green Tea</span><b>$3</b></li>
        <li><span>Coffee</span><b>$3</b></li>
        <li><span>Hot Chocolate</span><b>$4</b></li>
      </ul>
      <h2 class="section-title">SAKE</h2>
      <ul class="menu-table">
        <li class="head"><span>ITEMS</span><span>PRICE</span></li>
        <li><span>House Sake</span><b>$8</b></li>
        <li><span>Junmai Ginjo</span><b>$12</b></li>
        <li><span>Nigori Cloudy</span><b>$11</b></li>
        <li><span>Plum Sake</span><b>$9</b></li>
      </ul>
    </article>

    <article class="panel drink" style="left:326px">
      <div class="brand mini"><span class="mark"></span><span class="name">HARBORLINE</span><span class="sub">TOMA'S</span></div>
      <h2 class="section-title">WINE<small>by the glass</small></h2>
      <ul class="menu-table">
        <li class="head"><span>ITEMS</span><span>PRICE</span></li>
        <li><span>House Red</span><b>$8</b></li>
        <li><span>House White</span><b>$8</b></li>
        <li><span>Pinot Noir</span><b>$11</b></li>
        <li><span>Merlot</span><b>$10</b></li>
        <li><span>Cabernet</span><b>$11</b></li>
        <li><span>Chardonnay</span><b>$10</b></li>
        <li><span>Riesling</span><b>$9</b></li>
        <li><span>Prosecco</span><b>$10</b></li>
      </ul>
      <h2 class="section-title">WINE<small>by the bottle</small></h2>
      <ul class="menu-table">
        <li class="head"><span>ITEMS</span><span>PRICE</span></li>
        <li><span>Malbec</span><b>$38</b></li>
        <li><span>Syrah</span><b>$36</b></li>
        <li><span>Sauvignon Blanc</span><b>$34</b></li>
        <li><span>Pinot Grigio</span><b>$32</b></li>
        <li><span>Moscato</span><b>$30</b></li>
        <li><span>Rosé</span><b>$32</b></li>
        <li><span>Zinfandel</span><b>$36</b></li>
        <li><span>Champagne</span><b>$65</b></li>
      </ul>
    </article>

    <article class="panel drink" style="left:462px">
      <div class="brand mini"><span class="mark"></span><span class="name">HARBORLINE</span><span class="sub">TOMA'S</span></div>
      <h2 class="section-title">BOTTLED BEER</h2>
      <ul class="menu-table">
        <li class="head"><span>ITEMS</span><span>PRICE</span></li>
        <li><span>Harbor Lager</span><b>$6</b></li>
        <li><span>Jade Pale Ale</span><b>$7</b></li>
        <li><span>Red Lantern IPA</span><b>$7</b></li>
        <li><span>Dragon Stout</span><b>$7</b></li>
        <li><span>Pier Pilsner</span><b>$6</b></li>
        <li><span>Golden Junk Wheat</span><b>$7</b></li>
        <li><span>Tide Amber</span><b>$6</b></li>
        <li><span>Koi Light</span><b>$5</b></li>
        <li><span>Bamboo Blonde</span><b>$6</b></li>
        <li><span>Typhoon Porter</span><b>$7</b></li>
        <li><span>Sampan Sour</span><b>$8</b></li>
        <li><span>Lotus Cider</span><b>$7</b></li>
      </ul>
    </article>

    <article class="panel drink" style="left:598px">
      <div class="brand mini"><span class="mark"></span><span class="name">HARBORLINE</span><span class="sub">TOMA'S</span></div>
      <h2 class="section-title">COCKTAILS</h2>
      <ul class="menu-table">
        <li class="head"><span>ITEMS</span><span>PRICE</span></li>
        <li><span>Lychee Martini</span><b>$12</b></li>
        <li><span>Mai Tai</span><b>$11</b></li>
        <li><span>Ginger Mule</span><b>$11</b></li>
        <li><span>Plum Spritz</span><b>$10</b></li>
        <li><span>Dragon Sour</span><b>$12</b></li>
        <li><span>Jade Mojito</span><b>$11</b></li>
        <li><span>Lantern Punch</span><b>$10</b></li>
        <li><span>Yuzu Collins</span><b>$11</b></li>
        <li><span>Sake Sangria</span><b>$10</b></li>
        <li><span>Tea Old Fashioned</span><b>$13</b></li>
      </ul>
      <h2 class="section-title">LIQUOR<small>house</small></h2>
      <ul class="menu-table">
        <li class="head"><span>ITEMS</span><span>PRICE</span></li>
        <li><span>Vodka House</span><b>$7</b></li>
        <li><span>Gin House</span><b>$7</b></li>
        <li><span>Rum House</span><b>$7</b></li>
        <li><span>Tequila House</span><b>$8</b></li>
      </ul>
    </article>
  </section>

  <!-- LIQUOR PAGES -->
  <section class="row-liquor">
    <article class="panel drink" style="left:54px">
      <div class="brand mini"><span class="mark"></span><span class="name">HARBORLINE</span><span class="sub">TOMA'S</span></div>
      <h2 class="section-title">LIQUOR<small>vodka</small></h2>
      <ul class="menu-table">
        <li class="head"><span>ITEMS</span><span>PRICE</span></li>
        <li><span>Birch Vodka</span><b>$8</b></li>
        <li><span>Glacier Vodka</span><b>$9</b></li>
        <li><span>Steppe Vodka</span><b>$8</b></li>
        <li><span>Citrus Vodka</span><b>$8</b></li>
        <li><span>Reserve Vodka</span><b>$11</b></li>
        <li><span>Wheat Vodka</span><b>$9</b></li>
      </ul>
      <h2 class="section-title">LIQUOR<small>gin</small></h2>
      <ul class="menu-table">
        <li class="head"><span>ITEMS</span><span>PRICE</span></li>
        <li><span>Dock Gin</span><b>$8</b></li>
        <li><span>Juniper Gin</span><b>$9</b></li>
        <li><span>Botanic Gin</span><b>$10</b></li>
        <li><span>Navy Gin</span><b>$10</b></li>
        <li><span>Pink Gin</span><b>$9</b></li>
      </ul>
      <h2 class="section-title">LIQUOR<small>tequila</small></h2>
      <ul class="menu-table">
        <li class="head"><span>ITEMS</span><span>PRICE</span></li>
        <li><span>Blanco Tequila</span><b>$9</b></li>
        <li><span>Reposado Tequila</span><b>$10</b></li>
        <li><span>Añejo Tequila</span><b>$12</b></li>
        <li><span>Smoky Mezcal</span><b>$12</b></li>
      </ul>
    </article>

    <article class="panel drink" style="left:190px">
      <div class="brand mini"><span class="mark"></span><span class="name">HARBORLINE</span><span class="sub">TOMA'S</span></div>
      <h2 class="section-title">LIQUOR<small>rum</small></h2>
      <ul class="menu-table">
        <li class="head"><span>ITEMS</span><span>PRICE</span></li>
        <li><span>White Rum</span><b>$8</b></li>
        <li><span>Gold Rum</span><b>$8</b></li>
        <li><span>Dark Rum</span><b>$9</b></li>
        <li><span>Spiced Rum</span><b>$8</b></li>
        <li><span>Coconut Rum</span><b>$8</b></li>
        <li><span>Aged Rum</span><b>$12</b></li>
      </ul>
      <h2 class="section-title">LIQUOR<small>whiskey</small></h2>
      <ul class="menu-table">
        <li class="head"><span>ITEMS</span><span>PRICE</span></li>
        <li><span>Rye Whiskey</span><b>$10</b></li>
        <li><span>Corn Bourbon</span><b>$10</b></li>
        <li><span>Small Batch</span><b>$13</b></li>
        <li><span>Irish Blend</span><b>$9</b></li>
        <li><span>Japanese Blend</span><b>$14</b></li>
        <li><span>Honey Whiskey</span><b>$9</b></li>
      </ul>
    </article>

    <article class="panel drink" style="left:326px">
      <div class="brand mini"><span class="mark"></span><span class="name">HARBORLINE</span><span class="sub">TOMA'S</span></div>
      <h2 class="section-title">LIQUOR<small>scotch</small></h2>
      <ul class="menu-table">
        <li class="head"><span>ITEMS</span><span>PRICE</span></li>
        <li><span>Highland 12</span><b>$13</b></li>
        <li><span>Highland 18</span><b>$22</b></li>
        <li><span>Islay 10</span><b>$14</b></li>
        <li><span>Islay 16</span><b>$20</b></li>
        <li><span>Speyside 12</span><b>$13</b></li>
        <li><span>Speyside 15</span><b>$17</b></li>
        <li><span>Lowland 12</span><b>$12</b></li>
        <li><span>Campbell 10</span><b>$13</b></li>
        <li><span>Blended Reserve</span><b>$11</b></li>
        <li><span>Blended Gold</span><b>$15</b></li>
        <li><span>Cask Strength</span><b>$24</b></li>
        <li><span>Sherry Cask</span><b>$19</b></li>
      </ul>
    </article>

    <article class="panel drink" style="left:462px">
      <div class="brand mini"><span class="mark"></span><span class="name">HARBORLINE</span><span class="sub">TOMA'S</span></div>
    </article>
  </section>

</main>
</body>
</html>
```